Business Card and Letterhead for Nurlo - modern real estate business

I need a double sided business card design for Nurlo. Please see business card brief here https://papers.trelvimo.net/sheet/q/7XrTbaLeZpMmQ2uWvd9HkCj4yNoEfsGi3lRtAz_pk/view?mode=shared

Please feel free to design the business cards however you feel best. I am happy to give some creative freedoms and then provide feedback from there.

Please then also create a letterhead to match the business card design

Colors

Designer to choose colors to be used in the design.

Requirements
Must have
• Must be a modern, elegant business card which looks very professional

```html
<!DOCTYPE html>
<html lang="en">
<head>
<meta charset="utf-8">
<title>Nurlo – Business Card</title>
<link href="https://fonts.googleapis.com/css2?family=Poppins:wght@300;400;600&display=swap" rel="stylesheet">
<style>
  :root {
    --bg: #e9e8e6;
    --card-dark: #000000;
    --card-light: #ffffff;
    --brand-red: #e3202a;
    --ink: #111111;
    --ink-soft: #1c1c1c;
    --white: #ffffff;
    --portrait-top: #d8d4d0;
    --portrait-bottom: #2b2b2d;
  }
  * { margin: 0; padding: 0; box-sizing: border-box; }
  html, body { width: 1200px; height: 960px; overflow: hidden; }
  body {
    background: var(--bg);
    font-family: "Poppins", sans-serif;
    position: relative;
  }
  .card {
    position: absolute;
    width: 686px;
    height: 424px;
    box-shadow: 0 6px 18px rgba(0,0,0,0.18);
  }
  /* Back side */
  .card-back {
    left: 229px; top: 32px;
    background: var(--card-dark);
    color: var(--white);
    text-align: center;
  }
  .card-back .brand-name {
    position: absolute;
    left: 0; right: 0; top: 148px;
    font-size: 88px;
    font-weight: 600;
    line-height: 1;
    letter-spacing: 4px;
    color: var(--brand-red);
  }
  .card-back .company-licence {
    position: absolute;
    left: 0; right: 0; top: 246px;
    font-size: 19px;
    font-weight: 400;
    letter-spacing: 0.5px;
  }
  .card-back .postal-address,
  .card-back .contact-line {
    position: absolute;
    left: 0; right: 0;
    font-size: 12.5px;
    font-weight: 300;
    letter-spacing: 1px;
  }
  .card-back .postal-address { top: 356px; }
  .card-back .contact-line { top: 380px; }
  .card-back .contact-line .email { color: var(--brand-red); }

  /* Front side */
  .card-front {
    left: 231px; top: 496px;
    background: var(--card-light);
    color: var(--ink);
  }
  .card-front .brand-name {
    position: absolute;
    left: 39px; top: 60px;
    font-size: 64px;
    font-weight: 600;
    line-height: 1;
    letter-spacing: 3px;
    color: var(--brand-red);
  }
  .agent-details {
    position: absolute;
    left: 47px; top: 210px;
  }
  .agent-name {
    font-size: 24px;
    font-weight: 600;
    line-height: 1.2;
    color: var(--ink);
  }
  .agent-role, .agent-licence {
    font-size: 16px;
    font-weight: 300;
    line-height: 24px;
    color: var(--ink-soft);
  }
  .agent-contact {
    list-style: none;
    margin-top: 14px;
  }
  .agent-contact li {
    display: flex;
    align-items: center;
    gap: 8px;
    font-size: 17px;
    font-weight: 300;
    line-height: 24px;
  }
  .agent-contact svg { width: 11px; height: 11px; fill: var(--ink); }
  .agent-portrait {
    position: absolute;
    left: 305px; top: 28px;
    width: 370px; height: 396px;
    background: linear-gradient(180deg, var(--portrait-top) 0%, #8a7a70 28%, var(--portrait-bottom) 55%, #1a1a1c 100%);
    border-radius: 120px 120px 0 0;
  }
</style>
</head>
<body>
  <section class="card card-back">
    <div class="brand-name">NURLO</div>
    <p class="company-licence">Lic No. 10071284</p>
    <p class="postal-address">PO Box 7130 Ferndale NSW 2790</p>
    <p class="contact-line">02 4810 3927 | <span class="email">info@nurlo.com</span> | www.nurlo.com</p>
  </section>

  <section class="card card-front">
    <div class="brand-name">NURLO</div>
    <div class="agent-details">
      <h1 class="agent-name">Darren Pellow</h1>
      <p class="agent-role">Licenced Real Estate Agent</p>
      <p class="agent-licence">Lic No. 20318846</p>
      <ul class="agent-contact">
        <li>
          <svg viewBox="0 0 24 24" aria-hidden="true"><path d="M2 8c0-3 4-5 10-5s10 2 10 5v2h-5V8c-1-1-3-1.5-5-1.5S8 7 7 8v2H2z M5 12h14l2 9H3z"/></svg>
          0412 508 391
        </li>
        <li>
          <svg viewBox="0 0 24 24" aria-hidden="true"><path d="M2 5h20v14H2z M3 6l9 7 9-7" stroke="#fff" stroke-width="1.5"/></svg>
          darren@nurlo.com
        </li>
      </ul>
    </div>
    <div class="agent-portrait" role="img" aria-label="Portrait photo of the agent in a dark suit and shirt"></div>
  </section>
</body>
</html>
```